Conference Oversize Name Badge

Design an oversized name badge that would be worn by conference attendees using a lanyard.

Things to include on the name badge
- attendee's headshot (photo)
- attendee's first name and last name
- attendee's company name
- conference organizer company name
- conference organizer logo (attached)
- barcode
- attendee type color theme. For example: sponsor would have a red color theme, exhibitor would have blue color theme. Same badges but with different color themes.

Get creative!

Please let me know if you have any questions.

Industry/Entity Type

Event Planning

Requirements
Must have
• Whats important:
• 1. Attendee name and company name needs to be big and prominent and easily readable.
• 2. Incorporate attached conference organizer logo
• 3. Be creative
Should not have
• Please do not submit boring rectangle name badges.

```html
<!DOCTYPE html>
<html lang="en">
<head>
<meta charset="utf-8">
<title>Conference Oversize Name Badges</title>
<link rel="stylesheet" href="https://fonts.googleapis.com/css2?family=Source+Sans+3:wght@400;600&display=swap">
<style>
  :root {
    --canvas-bg: #000000;
    --badge-white: #ffffff;
    --sponsor-light: #e8696b;
    --sponsor-dark: #bd2c37;
    --sponsor-ink: #e8383d;
    --exhibitor-light: #2cb1e5;
    --exhibitor-dark: #1a74bd;
    --exhibitor-ink: #1a77bd;
  }
  html, body {
    margin: 0;
    padding: 0;
    width: 1200px;
    height: 800px;
    overflow: hidden;
    background: var(--canvas-bg);
  }
  .stage {
    position: relative;
    width: 1200px;
    height: 800px;
  }
  .badge {
    position: absolute;
    top: 258px;
    width: 283px;
    height: 283px;
  }
  .badge--sponsor { left: 256px; }
  .badge--exhibitor { left: 662px; }
  .badge svg { display: block; width: 100%; height: 100%; overflow: visible; }
  .badge text {
    font-family: "Source Sans 3", "Myriad Pro", sans-serif;
    font-weight: 600;
  }
  .badge__frame { fill: none; stroke: var(--badge-white); stroke-width: 8; stroke-linejoin: round; }
  .badge__id-card, .badge__dot { fill: var(--badge-white); }
  .badge__photo-ring { fill: none; stroke-width: 1.4; }
  .badge--sponsor .badge__photo-ring { stroke: var(--sponsor-ink); }
  .badge--exhibitor .badge__photo-ring { stroke: var(--exhibitor-ink); }
  .badge--sponsor .badge__ink { fill: var(--sponsor-ink); }
  .badge--exhibitor .badge__ink { fill: var(--exhibitor-ink); }
  .badge__label { fill: var(--badge-white); }
  .badge .stop-light-sponsor { stop-color: var(--sponsor-light); }
  .badge .stop-dark-sponsor { stop-color: var(--sponsor-dark); }
  .badge .stop-light-exhibitor { stop-color: var(--exhibitor-light); }
  .badge .stop-dark-exhibitor { stop-color: var(--exhibitor-dark); }
</style>
</head>
<body>
<main class="stage">

  <section class="badge badge--sponsor" aria-label="Sponsor badge">
    <svg viewBox="0 0 354 354">
      <defs>
        <linearGradient id="sponsor-fill" x1="0" y1="0" x2="0.4" y2="1">
          <stop offset="0" class="stop-light-sponsor"/>
          <stop offset="1" class="stop-dark-sponsor"/>
        </linearGradient>
      </defs>
      <path class="badge__body" fill="url(#sponsor-fill)" d="M150,4 Q177,-2 204,4 C260,20 330,90 350,150 Q356,177 350,204 C330,264 264,334 204,350 Q177,356 150,350 C90,334 20,264 4,204 Q-2,177 4,150 C20,90 90,20 150,4 Z"/>
      <path class="badge__frame" d="M150,22 C165,14 170,12 177,30 C184,12 189,14 204,22 C255,40 315,100 332,150 C340,165 342,170 324,177 C342,184 340,189 332,204 C315,255 255,315 204,332 C189,340 184,342 177,324 C170,342 165,340 150,332 C100,315 40,255 22,204 C14,189 12,184 30,177 C12,170 14,165 22,150 C40,100 100,40 150,22 Z"/>
      <path class="badge__id-card" d="M163,58 H240 V143 H163 A42.5,42.5 0 0 1 163,58 Z"/>
      <circle class="badge__photo-ring" cx="163" cy="101" r="35"/>
      <text class="badge__ink" x="163" y="107" font-size="17" text-anchor="middle">Photo</text>
      <text class="badge__ink" font-size="17" text-anchor="middle" transform="translate(226 101) rotate(-90)">Code</text>
      <text class="badge__label" x="181" y="170" font-size="17" text-anchor="middle">Attendee's name &amp; last name</text>
      <circle class="badge__dot" cx="89" cy="203" r="19"/>
      <text class="badge__label" x="115" y="207" font-size="17">Company logo &amp; name</text>
      <circle class="badge__dot" cx="177" cy="261" r="14"/>
      <text class="badge__label" x="177" y="303" font-size="17" text-anchor="middle">Organizer Name</text>
    </svg>
  </section>

  <section class="badge badge--exhibitor" aria-label="Exhibitor badge">
    <svg viewBox="0 0 354 354">
      <defs>
        <linearGradient id="exhibitor-fill" x1="0" y1="0" x2="0.4" y2="1">
          <stop offset="0" class="stop-light-exhibitor"/>
          <stop offset="1" class="stop-dark-exhibitor"/>
        </linearGradient>
      </defs>
      <path class="badge__body" fill="url(#exhibitor-fill)" d="M150,4 Q177,-2 204,4 C260,20 330,90 350,150 Q356,177 350,204 C330,264 264,334 204,350 Q177,356 150,350 C90,334 20,264 4,204 Q-2,177 4,150 C20,90 90,20 150,4 Z"/>
      <path class="badge__frame" d="M150,22 C165,14 170,12 177,30 C184,12 189,14 204,22 C255,40 315,100 332,150 C340,165 342,170 324,177 C342,184 340,189 332,204 C315,255 255,315 204,332 C189,340 184,342 177,324 C170,342 165,340 150,332 C100,315 40,255 22,204 C14,189 12,184 30,177 C12,170 14,165 22,150 C40,100 100,40 150,22 Z"/>
      <path class="badge__id-card" d="M163,58 H240 V143 H163 A42.5,42.5 0 0 1 163,58 Z"/>
      <circle class="badge__photo-ring" cx="163" cy="101" r="35"/>
      <text class="badge__ink" x="163" y="107" font-size="17" text-anchor="middle">Photo</text>
      <text class="badge__ink" font-size="17" text-anchor="middle" transform="translate(226 101) rotate(-90)">Code</text>
      <text class="badge__label" x="181" y="170" font-size="17" text-anchor="middle">Attendee's name &amp; last name</text>
      <circle class="badge__dot" cx="89" cy="203" r="19"/>
      <text class="badge__label" x="115" y="207" font-size="17">Company logo &amp; name</text>
      <circle class="badge__dot" cx="177" cy="261" r="14"/>
      <text class="badge__label" x="177" y="303" font-size="17" text-anchor="middle">Organizer Name</text>
    </svg>
  </section>

</main>
</body>
</html>
```